Logo for Quill Partners LLC needs a design

This logo will be for a food handler and restaurant manager training business located. I am a registered trainer and proctor for DineGuard, the United Kitchen Guild. colors options should be black, white, blue, silver or something else bold. The file that I have sent needs to be on the card somewhere, small.
Updates

need to have the DineGuard logo that I added on the card. QUILL stands for quality upkeep in local lunchrooms.

Logo Text

Dennis JonesStar ,Partners LLC. , Registered trainer and proctorwith DineGuard.

```html
<!DOCTYPE html>
<html lang="en">
<head>
<meta charset="UTF-8">
<title>Quill Partners LLC — Business Card</title>
<link href="https://fonts.googleapis.com/css2?family=Poppins:wght@400;600;700&family=Tinos:wght@700&display=swap" rel="stylesheet">
<style>
  :root {
    --stage: #2b2b2d;
    --navy: #233a92;
    --navy-deep: #1f3286;
    --ink: #26338f;
    --violet: #8a5fb0;
    --paper: #ffffff;
    --badge: #2e9fd8;
    --cert-ink: #4a4a4a;
  }
  * { margin: 0; padding: 0; box-sizing: border-box; }
  html, body { width: 1200px; height: 1108px; overflow: hidden; }
  body {
    background: var(--stage);
    font-family: "Poppins", sans-serif;
    position: relative;
  }
  .card {
    position: absolute;
    top: 194px;
    width: 420px;
    height: 720px;
    border-radius: 22px;
    overflow: hidden;
  }
  .card--front { left: 150px; background: var(--navy); }
  .card--back { left: 630px; background: var(--paper); text-align: center; }

  .wordmark {
    font-family: "Poppins", sans-serif;
    font-weight: 700;
    letter-spacing: 1px;
    display: flex;
    align-items: center;
    justify-content: center;
    gap: 10px;
  }
  .wordmark__dot { width: 14px; height: 14px; border-radius: 50%; }
  .card--front .wordmark {
    position: absolute; left: 0; right: 0; top: 330px;
    color: var(--paper); font-size: 30px;
  }
  .card--front .wordmark__dot { background: var(--paper); }
  .card--back .wordmark {
    margin-top: 120px; color: var(--ink); font-size: 30px;
  }
  .card--back .wordmark__dot { background: var(--violet); }

  .holder__name {
    margin-top: 42px; color: var(--ink);
    font-weight: 700; font-size: 26px; letter-spacing: .5px;
  }
  .holder__title {
    color: var(--violet); font-size: 14px; font-weight: 400;
    letter-spacing: 1px;
  }
  .rule {
    width: 16px; height: 2px; background: var(--violet);
    margin: 16px auto;
  }
  .contact__icons { display: flex; justify-content: center; gap: 6px; margin-bottom: 6px; }
  .contact__icons svg { width: 20px; height: 20px; }
  .contact__line { color: var(--ink); font-size: 17px; line-height: 1.35; }

  .cert { margin-top: 6px; }
  .cert__badge { width: 150px; height: 78px; margin: 0 auto; }
  .cert__text {
    font-family: "Tinos", serif; font-weight: 700;
    color: var(--cert-ink); font-size: 16px; line-height: 1.25;
    margin-top: 10px;
  }
</style>
</head>
<body>

<section class="card card--front" aria-label="Card front">
  <div class="wordmark"><span class="wordmark__dot"></span>QUILL PARTNERS LLC</div>
</section>

<section class="card card--back" aria-label="Card back">
  <div class="wordmark"><span class="wordmark__dot"></span>QUILL PARTNERS LLC</div>

  <h1 class="holder__name">HAROLD PIKE</h1>
  <p class="holder__title">PRESIDENT</p>
  <div class="rule"></div>

  <div class="contact">
    <div class="contact__icons">
      <svg viewBox="0 0 20 20" aria-label="Phone"><circle cx="10" cy="10" r="10" fill="var(--violet)"/><path d="M7 5.5l2 2-1 1.3c.6 1.3 1.6 2.3 2.9 2.9l1.3-1 2 2-1.2 1.6c-3.6-.4-6.8-3.6-7.2-7.2z" fill="#fff"/></svg>
      <svg viewBox="0 0 20 20" aria-label="Email"><circle cx="10" cy="10" r="10" fill="var(--violet)"/><rect x="5" y="6.5" width="10" height="7" rx="1" fill="#fff"/><path d="M5.5 7l4.5 3.5L14.5 7" stroke="var(--violet)" stroke-width="1" fill="none"/></svg>
      <svg viewBox="0 0 20 20" aria-label="Website"><circle cx="10" cy="10" r="10" fill="var(--violet)"/><circle cx="10" cy="10" r="5" fill="none" stroke="#fff" stroke-width="1.2"/><ellipse cx="10" cy="10" rx="2.2" ry="5" fill="none" stroke="#fff" stroke-width="1"/><path d="M5 10h10" stroke="#fff" stroke-width="1"/></svg>
    </div>
    <p class="contact__line">555-014-2290</p>
    <p class="contact__line">quillpartnersllc@inboxmail.net</p>
    <p class="contact__line">quillpartnersllc.com</p>
  </div>
  <div class="rule"></div>

  <div class="cert">
    <svg class="cert__badge" viewBox="0 0 150 78" role="img" aria-label="DineGuard certification badge">
      <ellipse cx="75" cy="39" rx="70" ry="34" fill="none" stroke="var(--badge)" stroke-width="4"/>
    </svg>
    <p class="cert__text">Registered DineGuard Proctor<br>&amp; Certified DineGuard Instructor</p>
  </div>
</section>

</body>
</html>
```